Dean Hollis Business Card

In addition to my name design (file uploaded), black print on white card stock, e-mail address should be presented as a typical e-mail address, i.e., underlined and in blue ink, the card should include the following information:
Professor of Aviation Technology
Accident Litigation Expert Witness
Master Certificated Flight Instructor

dhollis@vexmail.example
Anchorage, Alaska
(907) 318-5074

```html
<!DOCTYPE html>
<html lang="en">
<head>
<meta charset="utf-8">
<title>Dean Hollis Business Card</title>
<link rel="stylesheet" href="https://fonts.googleapis.com/css2?family=Bebas+Neue&family=Roboto:wght@400&display=swap">
<style>
  :root {
    --page-bg: #e4e4e4;
    --card-bg: #ffffff;
    --ink: #1e1c1c;
    --accent: #3b3a86;
    --band: #3f52a4;
    --band-text: #ffffff;
    --rule: #9a9a9a;
  }
  html, body {
    margin: 0;
    width: 1200px;
    height: 1200px;
    overflow: hidden;
    background: var(--page-bg);
  }
  .card {
    position: absolute;
    left: 60px;
    top: 284px;
    width: 1080px;
    height: 632px;
    background: var(--card-bg);
  }
  .name {
    position: absolute;
    left: 0;
    right: 0;
    top: 126px;
    margin: 0;
    text-align: center;
    font-family: "Bebas Neue", "Arial Narrow", sans-serif;
    font-weight: 400;
    font-size: 146px;
    line-height: 1;
    letter-spacing: 4px;
    color: var(--ink);
  }
  .credentials {
    position: absolute;
    left: 0;
    right: 0;
    top: 280px;
    margin: 0;
    padding: 0;
    list-style: none;
    display: flex;
    justify-content: center;
    align-items: center;
    gap: 12px;
    font-family: "Roboto", Arial, sans-serif;
    font-size: 17px;
    color: var(--accent);
  }
  .credentials .dot {
    width: 8px;
    height: 8px;
    border-radius: 50%;
    background: #7b78b8;
  }
  .divider {
    position: absolute;
    left: 113px;
    right: 113px;
    top: 318px;
    border: 0;
    border-top: 1px dashed var(--rule);
    margin: 0;
  }
  .contact-band {
    position: absolute;
    left: 0;
    right: 0;
    top: 471px;
    height: 43px;
    background: var(--band);
    display: flex;
    justify-content: center;
    align-items: center;
    gap: 14px;
    font-family: "Roboto", Arial, sans-serif;
    font-size: 22px;
    color: var(--band-text);
  }
  .contact-band .dot {
    width: 7px;
    height: 7px;
    border-radius: 50%;
    background: var(--band-text);
  }
  .contact-band a {
    color: inherit;
    text-decoration: none;
  }
</style>
</head>
<body>
  <div class="card">
    <h1 class="name">DEAN E. HOLLIS</h1>
    <ul class="credentials">
      <li>Professor of Aviation Technology</li>
      <li class="dot" aria-hidden="true"></li>
      <li>Accident Litigation Expert Witness</li>
      <li class="dot" aria-hidden="true"></li>
      <li>Master Certificated Flight Instructor</li>
    </ul>
    <hr class="divider">
    <div class="contact-band">
      <a class="email" href="mailto:dhollis@vexmail.example">dhollis@vexmail.example</a>
      <span class="dot" aria-hidden="true"></span>
      <span class="location">Anchorage, Alaska</span>
      <span class="dot" aria-hidden="true"></span>
      <span class="phone">(907) 318-5074</span>
    </div>
  </div>
</body>
</html>
```